Aisle signage for supermarket

Design Isle signs for Indian supermarket. Modern, Clear, legible. Would be nice to use our logo colours. Signs Will be double sided and measure 900mm width x 400mm height. Indian theme would be nice. Attached files shows description to go on each sign.
Font styles to use
Sans Serif
Colors
Designer to choose colors to be used in the design.

```html
<!DOCTYPE html>
<html lang="en">
<head>
<meta charset="utf-8">
<title>Aisle Sign – Biscuits, Tea, Savouries</title>
<link href="https://fonts.googleapis.com/css2?family=Josefin+Sans:wght@700&display=swap" rel="stylesheet">
<style>
  :root {
    --backdrop: #242424;
    --sign: #ffffff;
    --ink: #222222;
    --leaf-dark: #35683b;
    --leaf-light: #9dc44d;
    --pattern-tone: #e6e6e6;
  }
  html, body {
    margin: 0;
    padding: 0;
    width: 1200px;
    height: 686px;
    overflow: hidden;
    background: var(--backdrop);
  }
  .aisle-sign {
    position: absolute;
    left: 47px;
    top: 98px;
    width: 1107px;
    height: 492px;
    background: var(--sign);
    overflow: hidden;
  }
  .line-pattern {
    position: absolute;
    left: 160px;
    top: 0;
    width: 947px;
    height: 492px;
    background: radial-gradient(ellipse at 40% 45%, var(--pattern-tone) 0%, rgba(230,230,230,0.5) 40%, rgba(255,255,255,0) 75%);
  }
  .sign-bands {
    position: absolute;
    inset: 0;
  }
  .sign-frame {
    position: absolute;
    left: 40px;
    top: 31px;
    width: 1012px;
    height: 434px;
    border: 4px solid var(--ink);
  }
  .category-list {
    position: absolute;
    left: 79px;
    top: 51px;
    margin: 0;
    padding: 0;
    list-style: none;
    font-family: "Josefin Sans", sans-serif;
    font-weight: 700;
    font-size: 60px;
    line-height: 130px;
    color: var(--ink);
    white-space: nowrap;
    text-shadow:
      3px 0 0 var(--sign), -3px 0 0 var(--sign),
      0 3px 0 var(--sign), 0 -3px 0 var(--sign),
      2px 2px 0 var(--sign), -2px -2px 0 var(--sign),
      2px -2px 0 var(--sign), -2px 2px 0 var(--sign);
  }
  .category-list li { height: 130px; }
  .store-name {
    position: absolute;
    left: 715px;
    top: 400px;
    width: 330px;
    text-align: center;
    white-space: nowrap;
    font-family: "Josefin Sans", sans-serif;
    font-weight: 700;
    font-size: 30px;
    letter-spacing: 3px;
    color: var(--leaf-dark);
  }
</style>
</head>
<body>
  <section class="aisle-sign">
    <div class="line-pattern" role="img" aria-label="Fine grey string-art line pattern fanning across the sign"></div>
    <svg class="sign-bands" viewBox="0 0 1107 492" width="1107" height="492" aria-hidden="true">
      <g fill="none">
        <path d="M-10 44 C 250 120, 430 230, 427 500" stroke="var(--leaf-light)" stroke-width="50"/>
        <path d="M-10 212 C 180 270, 300 350, 304 500" stroke="var(--leaf-dark)" stroke-width="72"/>
        <path d="M995 -5 C 1000 80, 1050 125, 1115 150" stroke="var(--leaf-light)" stroke-width="62"/>
        <path d="M887 -5 C 880 150, 980 240, 1115 300" stroke="var(--leaf-dark)" stroke-width="40"/>
      </g>
    </svg>
    <div class="sign-frame"></div>
    <ul class="category-list">
      <li>BISCUITS / CAKES</li>
      <li>TEA / COFFEE</li>
      <li>SAVOURIES</li>
    </ul>
    <div class="store-name">KAVYA GROCERS</div>
  </section>
</body>
</html>
```